Postcard Design

New Youth Tackle and Youth football program in Austin Texas named Brookmere Football Academy. The program will offer both Spring 7-on-7 and Fall Tackle football. WE need to market the program. The website is www.BrookmereFootballAcademy.example the phone number for the program is (512) 555-0147. Also, This is AMERICAN football NOT soccer. I want to use this as a mailer so the back side of the postcard needs room for an address but should still have some color and advertising on it.

```html
<!DOCTYPE html>
<html lang="en">
<head>
<meta charset="utf-8">
<title>Brookmere Football Academy Postcard</title>
<link rel="stylesheet" href="https://fonts.googleapis.com/css2?family=Alfa+Slab+One&family=Alegreya:wght@400;700&family=Alegreya+SC:wght@700&display=swap">
<style>
  :root {
    --bg: #d9d9d9;
    --paper: #ffffff;
    --red: #e0262b;
    --orange: #ee5a2a;
    --blue: #2b43a8;
    --blue-light: #3a5bd0;
    --ink: #1f2a6b;
    --brown: #6b2a1f;
    --brown-light: #8a4030;
  }
  * { box-sizing: border-box; margin: 0; padding: 0; }
  html, body { width: 1200px; height: 800px; overflow: hidden; }
  body { background: var(--bg); font-family: "Alegreya", serif; position: relative; }

  .card { position: absolute; top: 210px; width: 560px; height: 380px; box-shadow: 0 6px 18px rgba(0,0,0,.18); }

  /* Back side */
  .card--back { left: 20px; background: var(--paper); }
  .back-frame { position: absolute; inset: 12px; border: 3px solid var(--red); }
  .back-brand { position: absolute; left: 30px; top: 40px; width: 260px; text-align: center; }
  .back-brand__name { font-family: "Alfa Slab One", serif; color: var(--red); font-size: 30px; line-height: 1; letter-spacing: .5px; }
  .back-brand__sub { font-family: "Alfa Slab One", serif; color: var(--red); font-size: 18px; line-height: 1.15; }
  .back-copy { position: absolute; left: 30px; top: 132px; width: 262px; font-size: 13.5px; line-height: 1.3; color: var(--ink); text-align: justify; }
  .back-contact { position: absolute; left: 30px; top: 298px; font-size: 14px; color: var(--ink); }
  .back-contact li { list-style: none; display: flex; align-items: center; gap: 10px; margin-bottom: 6px; }
  .back-contact svg { width: 16px; height: 16px; flex: none; }
  .stamp-box { position: absolute; right: 36px; top: 32px; width: 66px; height: 76px; border: 1.5px solid var(--blue); }
  .address-divider { position: absolute; left: 312px; top: 120px; height: 150px; border-left: 1.5px solid var(--blue); opacity: .7; }
  .address-line { position: absolute; left: 312px; right: 36px; border-top: 1.5px solid var(--blue); opacity: .7; }

  /* Front side */
  .card--front { left: 620px; overflow: hidden; background: var(--red); }
  .front-half { position: absolute; top: 0; bottom: 0; width: 280px; }
  .front-half--left { left: 0; background: var(--red); }
  .front-half--right { right: 0; background: var(--blue); border-left: 3px solid #fff; }
  .front-glow--left { position: absolute; inset: 0 0 95px 0; background: radial-gradient(circle at 45% 55%, var(--orange), var(--red) 75%); }
  .front-glow--right { position: absolute; inset: 0; background: radial-gradient(circle at 50% 45%, var(--blue-light), var(--blue) 70%); }
  .emblem { position: absolute; width: 150px; height: 130px; border-radius: 14px; background: linear-gradient(180deg, rgba(255,255,255,.35), rgba(255,255,255,.15)); }
  .emblem--spring { left: 62px; top: 150px; }
  .emblem--fall { left: 62px; top: 90px; }
  .band { position: absolute; color: #fff; font-family: "Alegreya SC", serif; font-size: 17px; letter-spacing: 1px; display: flex; align-items: center; justify-content: center; }
  .band--spring { left: 0; width: 280px; top: 290px; height: 32px; background: var(--blue); }
  .band--fall { left: 0; width: 280px; top: 222px; height: 32px; background: var(--red); }
  .football-art { position: absolute; left: 248px; top: 192px; width: 66px; height: 50px; border-radius: 6px; background: linear-gradient(180deg, var(--brown-light), var(--brown)); }
  .and-tag { position: absolute; left: 240px; top: 248px; width: 84px; height: 30px; background: #fff; color: var(--ink); font-family: "Alegreya SC", serif; font-size: 15px; display: flex; align-items: center; justify-content: center; box-shadow: 0 2px 4px rgba(0,0,0,.3); }
  .pennant { position: absolute; left: 122px; top: 0; width: 320px; height: 140px; }
  .pennant__brand { position: absolute; left: 0; right: 0; top: 30px; text-align: center; font-family: "Alegreya", serif; font-weight: 700; font-size: 12px; color: var(--blue); }
  .pennant__line1 { position: absolute; left: 0; right: 0; top: 48px; text-align: center; font-family: "Alfa Slab One", serif; font-size: 20px; line-height: 1.2; color: var(--red); }
  .pennant__line2 { position: absolute; left: 0; right: 0; top: 74px; text-align: center; font-family: "Alfa Slab One", serif; font-size: 22px; line-height: 1.2; color: var(--blue); }
</style>
</head>
<body>

<section class="card card--back" aria-label="Postcard back">
  <div class="back-frame"></div>
  <div class="back-brand">
    <div class="back-brand__name">BROOKMERE</div>
    <div class="back-brand__sub">FOOTBALL ACADEMY</div>
  </div>
  <p class="back-copy">Our program is built around four core values: Honesty, Integrity, Respect, &amp; Transparency. We will focus on the process of bringing success—both on the field and outside the lines. We strive for maximum involvement from families, stakeholders and players.</p>
  <ul class="back-contact">
    <li>
      <svg viewBox="0 0 16 16" aria-hidden="true"><path fill="#1f2a6b" d="M3.5 1.5l2.4 2.8-1.3 1.7c.9 2 2.5 3.6 4.5 4.5l1.7-1.3 2.8 2.4-1.6 2.4C7 13.6 2.4 9 1.1 3.1z"/></svg>
      (512) 555-0147
    </li>
    <li>
      <svg viewBox="0 0 16 16" aria-hidden="true"><circle cx="8" cy="8" r="7" fill="#2b43a8"/><path d="M1 8h14M8 1c-3 3.5-3 10.5 0 14M8 1c3 3.5 3 10.5 0 14" stroke="#fff" stroke-width="1" fill="none"/></svg>
      www.BrookmereFootballAcademy.example
    </li>
  </ul>
  <div class="stamp-box"></div>
  <div class="address-divider"></div>
  <div class="address-line" style="top:160px"></div>
  <div class="address-line" style="top:200px"></div>
  <div class="address-line" style="top:240px"></div>
</section>

<section class="card card--front" aria-label="Postcard front">
  <div class="front-half front-half--left">
    <div class="front-glow--left"></div>
    <div class="emblem emblem--spring" role="img" aria-label="Laurel wreath around a 7 on 7 football emblem"></div>
    <div class="band band--spring">Spring 7 on 7</div>
  </div>
  <div class="front-half front-half--right">
    <div class="front-glow--right"></div>
    <div class="emblem emblem--fall" role="img" aria-label="Laurel wreath around a football helmet"></div>
    <div class="band band--fall">Fall Tackle Football</div>
  </div>
  <div class="football-art" role="img" aria-label="Illustration of an American football"></div>
  <div class="and-tag">AND</div>
  <div class="pennant">
    <svg width="320" height="140" viewBox="0 0 320 140" aria-hidden="true">
      <path d="M0 0H320V112L160 138L0 112Z" fill="#2b43a8"/>
      <path d="M5 0H315V108L160 133L5 108Z" fill="#e0262b"/>
      <path d="M10 0H310V104L160 128L10 104Z" fill="#ffffff"/>
      <path d="M16 20H304V98L160 120L16 98Z" fill="none" stroke="#2b43a8" stroke-width="1.5"/>
    </svg>
    <div class="pennant__brand">BROOKMERE</div>
    <div class="pennant__line1">ALL ARE WELCOME</div>
    <div class="pennant__line2">COME JOIN US!!</div>
  </div>
</section>

</body>
</html>
```